Accountancy practice needs a wordpress website redesign for growth

We are a growing accountancy practice - headcount and revenues have doubled in the last 2 years. We are continuing to grow. We only had a website made around 12 months ago but the company we used offered very little in terms of creativity and ideas of how to make it look modern and eye-catching. We want to redesign the website to make it look premium and professional because we are starting to launch more marketing and drive more traffic to the site.

The current website is www.tovelbrookaccountants.co.uk. The website was built in wordpress.

The logo has been uploaded. The main 2 colour hex codes are: 0E74BC and 14A79D.

We are open to changing the fonts in the website and welcome suggestions for this too.

Following on from this we will launch a project to design brochures and one-page flyers that we can fill with useful information about what we do and also create lead-generators to download from the website. So the design of the website will influence the overall brand and feel of all of the marketing collateral.

Target Market(s)

Property businesses and entrepreneurial, growth mindset clients

Industry/Entity Type

Accountancy

Number of Pages Required

3 page

Font styles to use
Sans Serif

Colors

Designer to choose colors to be used in the design.

Requirements
Must have
• A modern and professional feel. 3 fonts - most websites seem to use 3 different fonts now and I like this. We have our green and blue colours but I do not want too much of this all over the site, stick to blacks, whites and greys with the blue and green used for emphasis and accents.
Nice to have
• The coloured spaces should have some "depth" to them, eg a small pattern in the white spaces so its not just a solid whie background.

```html
<!DOCTYPE html>
<html lang="en">
<head>
<meta charset="utf-8">
<title>Tovelbrook Accountants</title>
<link href="https://fonts.googleapis.com/css2?family=Lexend:wght@400;500;600&family=Roboto:ital,wght@0,400;0,500;0,700;1,400&display=swap" rel="stylesheet">
<style>
:root{
  --blue:#0E74BC;
  --teal:#14A79D;
  --ink:#111418;
  --text:#4a4f55;
  --grey-bg:#f6f6f7;
  --line:#e4e6ea;
  --white:#ffffff;
}
*{margin:0;padding:0;box-sizing:border-box}
html,body{width:1200px;height:4005px;overflow:hidden}
body{position:relative;background:var(--white);font-family:'Roboto',sans-serif;color:var(--ink)}
.abs{position:absolute}
.heading{font-family:'Lexend',sans-serif;font-weight:500;color:var(--ink)}
.btn{position:absolute;display:flex;align-items:center;justify-content:center;font-family:'Lexend',sans-serif;font-weight:500;font-size:15px;border-radius:2px}
.btn-teal{background:var(--teal);color:var(--white)}
.btn-white{background:var(--white);color:var(--ink)}
.brand{font-family:'Roboto',sans-serif;font-weight:700;font-size:20px;line-height:22px;letter-spacing:.5px;display:flex;align-items:center;gap:10px}
.brand-mark{width:26px;height:26px;background:var(--teal);flex:none}

/* header / hero */
.hero-bg{left:0;top:0;width:1200px;height:482px;background:var(--grey-bg)}
.corner{left:0;top:0}
.nav a{position:absolute;top:44px;font-size:16px;color:var(--ink);text-decoration:none;font-family:'Roboto',sans-serif}
.hero-title{left:90px;top:168px;font-size:46px;line-height:55px;width:520px}
.hero-photo{left:609px;top:155px;width:446px;height:327px;background:linear-gradient(135deg,#cfd6de 0%,#8c99a8 45%,#e9ecef 100%)}

/* software */
.soft-title{left:0;top:574px;width:1200px;text-align:center;font-size:31px}
.soft-copy{left:150px;top:629px;width:900px;text-align:center;font-size:11.5px;line-height:14px;color:var(--text)}
.logo-strip{left:78px;top:676px;width:1056px;height:148px;background:var(--white);box-shadow:0 18px 30px rgba(0,0,0,.06)}
.partner{position:absolute;top:735px;font-family:'Roboto',sans-serif;font-weight:500;font-size:27px;color:#5d646c;display:flex;align-items:center;gap:8px}
.partner .dot{width:22px;height:22px;border-radius:50%;background:#5d646c}
.partner.faded{color:#c9ced4}

/* about band */
.about-band{left:0;top:970px}
.about-img{position:absolute}
.about-title{left:618px;top:1036px;font-size:30px;color:var(--white);font-weight:500;letter-spacing:.3px}
.about-copy{left:618px;top:1096px;width:518px;font-size:14px;line-height:18.5px;font-weight:700;color:#eaf7f6}
.about-lead{left:618px;top:1223px;font-size:15.5px;font-weight:500;color:var(--white)}
.pattern{background:radial-gradient(ellipse at center,rgba(180,186,194,.22),rgba(180,186,194,0) 70%)}

/* who we help */
.help-title{left:0;top:1625px;width:1200px;text-align:center;font-size:33px}
.help-card{position:absolute;top:1702px;width:241px;height:245px;background:var(--white);box-shadow:0 6px 24px rgba(0,0,0,.07);text-align:center}
.help-card svg{position:absolute;left:50%;transform:translateX(-50%);top:50px}
.help-card h3{position:absolute;left:0;width:100%;font-size:12.5px;font-weight:700;font-family:'Roboto',sans-serif}
.help-card p{position:absolute;left:30px;width:181px;font-size:11.5px;line-height:14px;color:var(--text)}
.help-card .more{position:absolute;left:0;width:100%;top:199px;font-size:12px;color:var(--ink)}

/* why */
.why{left:0;top:2095px;width:1200px;height:373px;background:var(--blue);color:var(--white)}
.why-title{left:90px;top:2150px;font-size:32px;color:var(--white)}
.why-lead{left:90px;top:2213px;width:660px;font-size:16px;line-height:20px;color:var(--white)}
.why-small{left:90px;top:2271px;width:620px;font-size:11.5px;line-height:17.5px;color:#d6e8f5}
.why-right{left:763px;top:2140px;width:360px;color:#d6e8f5;font-size:11.5px;line-height:17.5px}
.why-right h4{font-family:'Roboto',sans-serif;font-weight:400;font-size:16px;color:var(--white);margin-bottom:10px}
.why-right ul{list-style:none}
.why-right li{position:relative;padding-left:12px}
.why-right li::before{content:"•";position:absolute;left:0}
.why-right p{margin-top:12px;padding-left:2px}

/* insights */
.insight-title{left:0;top:2558px;width:1200px;text-align:center;font-size:33px}
.post{position:absolute;top:2647px;width:463px;height:438px;background:var(--white);box-shadow:0 10px 30px rgba(0,0,0,.06)}
.post-img{position:absolute;left:0;top:0;width:463px;height:239px}
.post h3{position:absolute;left:0;top:273px;width:463px;font-family:'Roboto',sans-serif;font-weight:700;font-size:15px;line-height:21px;text-transform:uppercase}
.post p{position:absolute;left:0;top:325px;width:463px;font-size:12px;line-height:18.5px;color:var(--text)}
.post .more{position:absolute;left:0;top:391px;font-size:13.5px;font-weight:500;color:var(--ink)}

/* feedback */
.feedback{left:0;top:3178px;width:1200px;height:368px;background:var(--grey-bg)}
.reviewer{left:239px;top:3240px;width:219px;height:288px;background:var(--white);text-align:center}
.avatar{position:absolute;left:69px;top:61px;width:80px;height:80px;border-radius:50%;background:linear-gradient(160deg,#9aa1a8,#4e555c)}
.reviewer .role{position:absolute;left:0;top:160px;width:100%;font-size:11.5px;color:var(--text)}
.reviewer .name{position:absolute;left:0;top:177px;width:100%;font-size:13px;font-weight:500}
.fb-title{left:496px;top:3287px;font-size:35px}
.fb-quote{left:496px;top:3354px;width:470px;font-size:12px;line-height:18.5px;font-style:italic;color:var(--text)}
.stars{left:496px;top:3415px}
.pager{left:496px;top:3455px;display:flex;gap:8px}
.pager span{display:block;width:14px;height:3px;background:#cfd3d8}
.pager span.on{width:34px;background:var(--teal)}

/* cta */
.cta{left:127px;top:3643px;width:945px;height:115px;background:var(--teal)}
.cta-title{left:182px;top:3676px;font-size:23px;color:var(--white)}
.cta-sub{left:182px;top:3713px;font-size:13px;font-weight:700;color:var(--white)}

/* footer */
.footer{left:0;top:3772px;width:1200px;height:233px;background:var(--blue)}
.foot-contact{left:164px;font-size:12.5px;color:var(--white);display:flex;align-items:center;gap:14px}
.foot-head{font-family:'Lexend',sans-serif;font-weight:400;font-size:18px;color:var(--white)}
.foot-link{left:531px;font-size:12.5px;color:#e3eef8}
.email{left:825px;top:3876px;width:187px;height:30px;background:var(--white);font-size:9px;color:#888;padding:10px 14px}
.signup{left:1012px;top:3876px;width:98px;height:30px;background:var(--teal);color:var(--white);font-size:12px;font-weight:500;display:flex;align-items:center;justify-content:center}
.foot-rule{left:148px;top:3966px;width:1052px;height:1px;background:rgba(255,255,255,.25)}
.foot-bottom{top:3977px;font-size:15px;font-weight:500;color:var(--white)}
</style>
</head>
<body>

<!-- header & hero -->
<div class="abs hero-bg"></div>
<svg class="abs corner" width="1200" height="160" aria-hidden="true"><polygon points="951,0 1200,0 1200,75 1105,148" fill="var(--blue)"/></svg>
<div class="abs brand" style="left:90px;top:40px;color:var(--blue)"><span class="brand-mark"></span>Tovelbrook<br>Accountants</div>
<nav class="nav">
  <a style="left:281px">About Us</a>
  <a style="left:398px">Who We Help</a>
  <a style="left:545px">Thoughts</a>
  <a style="left:667px">Switching Accountants</a>
</nav>
<div class="btn btn-teal" style="left:866px;top:34px;width:216px;height:41px">Book A Discovery Call</div>
<h1 class="abs heading hero-title">Your Accounts Will Be Done.What Else Can We Do For You?</h1>
<div class="btn btn-teal" style="left:90px;top:362px;width:272px;height:42px">Book A Discovery Call Now</div>
<div class="abs hero-photo" role="img" aria-label="Photo of accountants in a meeting reviewing charts at an office desk"></div>

<!-- software -->
<h2 class="abs heading soft-title">Software Solutions</h2>
<p class="abs soft-copy">We are proud to work with a range of software solutions to ensure your accountancy procedures are running as smoothly as possible. Software can make a significant difference to your business and through the use of these solutions we can save you time and money, whilst also improving your business efficiency.</p>
<div class="abs logo-strip"></div>
<div class="partner faded" style="left:0">Ledgerpay</div>
<div class="partner" style="left:160px"><span class="dot"></span>Callroom</div>
<div class="partner" style="left:300px">ScanEntry</div>
<div class="partner" style="left:524px">Linkbot</div>
<div class="partner" style="left:688px">Wagewell</div>
<div class="partner" style="left:880px">Staffly</div>
<div class="partner faded" style="left:1052px">Debitflow</div>

<!-- about band -->
<div class="abs pattern" style="left:0;top:1360px;width:360px;height:720px" role="img" aria-label="Faint dotted pattern"></div>
<div class="abs pattern" style="left:900px;top:1180px;width:300px;height:420px" role="img" aria-label="Faint dotted pattern"></div>
<svg class="abs about-band" width="1200" height="540" aria-hidden="true"><polygon points="0,0 1200,0 1200,188 536,537 0,382" fill="var(--teal)"/></svg>
<div class="about-img" style="left:126px;top:951px;width:208px;height:230px;background:linear-gradient(150deg,#e6e9ec,#7b8692 60%,#d3d8dd)" role="img" aria-label="Photo of a businesswoman in a meeting"></div>
<div class="about-img" style="left:89px;top:1204px;width:247px;height:249px;background:linear-gradient(160deg,#5f6770,#c9cdd1 60%,#8a9097)" role="img" aria-label="Photo of a tablet beside architectural building models"></div>
<div class="about-img" style="left:353px;top:1018px;width:245px;height:278px;background:linear-gradient(140deg,#eef1f4,#a5b0bb 55%,#5b6773)" role="img" aria-label="Photo of two colleagues reviewing work on a laptop"></div>
<h2 class="abs about-title">TOVELBROOK ACCOUNTANTS</h2>
<p class="abs about-copy">We understand that running and growing your business takes an incredible amount of effort; you don't want to be bogged down worrying about getting paperwork done on time. You want to know that the decisions you make are based on sound, correct advice and you want to be able to talk to someone you trust for that advice. So don't worry – we will make sure your accounts and taxes are done</p>
<p class="abs about-lead">Let's see what else we can do for you.</p>
<div class="btn btn-white" style="left:618px;top:1259px;width:218px;height:40px">Get In Touch</div>

<!-- who we help -->
<h2 class="abs heading help-title">Who We Help</h2>
<div class="help-card" style="left:85px">
  <svg width="56" height="56" viewBox="0 0 56 56" fill="none" stroke="var(--blue)" stroke-width="2"><rect x="6" y="16" width="22" height="36"/><rect x="28" y="6" width="22" height="46"/><path d="M11 24h4M19 24h4M11 32h4M19 32h4M11 40h4M19 40h4M33 14h4M41 14h4M33 22h4M41 22h4M33 30h4M41 30h4M36 52v-10h6v10"/></svg>
  <h3 style="top:128px">Property Investors &amp; Developers</h3>
  <p style="top:145px">Busy with your investments and need to ensure your accounts are in order?</p>
  <span class="more">Read More</span>
</div>
<div class="help-card" style="left:353px">
  <svg width="60" height="56" viewBox="0 0 60 56" fill="none" stroke="var(--blue)" stroke-width="2"><path d="M24 6h30v22H40l-8 7v-7h-8z"/><path d="M30 13h18M30 20h14"/><circle cx="20" cy="34" r="15"/><path d="M16 30a4 4 0 1 1 5 4v3M20 41v1"/></svg>
  <h3 style="top:142px">Consultants</h3>
  <p style="top:160px">Your time is precious. Allow us to free up more of your valuable time.</p>
  <span class="more">Read More</span>
</div>
<div class="help-card" style="left:608px">
  <svg width="56" height="60" viewBox="0 0 56 60" fill="none" stroke="var(--blue)" stroke-width="2"><path d="M10 4v14a10 10 0 0 0 20 0V4"/><path d="M20 28v14a10 10 0 0 0 20 0v-6"/><circle cx="40" cy="31" r="5"/></svg>
  <h3 style="top:142px">Medical Professionals</h3>
  <p style="top:160px">We take care of you whilst you take care of your patients.</p>
  <span class="more">Read More</span>
</div>
<div class="help-card" style="left:869px">
  <svg width="64" height="48" viewBox="0 0 64 48" fill="none" stroke="var(--blue)" stroke-width="2"><path d="M2 12l10-4 10 20-8 4z"/><path d="M62 12l-10-4-10 20 8 4z"/><path d="M22 14l10-4 10 4M14 30l10 10c2 2 5 2 7 0l13-12"/><path d="M24 34l6 6M29 30l6 6"/></svg>
  <h3 style="top:128px">Buying or selling a business</h3>
  <p style="top:145px">When buying or selling a business you need to know you have the right people in your corner.</p>
  <span class="more">Read More</span>
</div>

<!-- why choose us -->
<div class="abs why"></div>
<h2 class="abs heading why-title">Why Choose Us?</h2>
<p class="abs why-lead">At Tovelbrook Accountants, we know you are the kind of people who want to be successful and have the time to do the things you love doing and to see the people you love seeing.</p>
<p class="abs why-small">To do that, you need to focus on the important issues in your business and know that the numbers and filing deadlines are taken care of. You also need to know that you are getting reliable feedback and advice that can be used to make decisions.<br>The problem is (and we hear it from a lot of people) that the current accountant only does numbers and nothing else, or they don't reply to you, or they don't offer any solutions, or... Whatever the problem is, the end result is you are micromanaging and not getting the results you want.</p>
<div class="btn btn-white" style="left:472px;top:2371px;width:255px;height:41px">Book An Appointmengt Now</div>
<div class="abs why-right">
  <h4>Relax, we've got this covered.</h4>
  <ul>
    <li>We're here at the end of the phone to talk you through those decisions – you'll have a dedicated point of contact (you can even pick how senior you want your contact to be).</li>
    <li>We'll make sure your deadlines aren't missed.</li>
    <li>We'll tell you if we think we aren't doing things in the best way possible.</li>
    <li>We'll even attend your board meetings, if you'd like, to get into the business and provide that detailed input you are looking for.</li>
  </ul>
  <p>If that sounds like the relationship you want, then book a video call with us. Then you can start doing the things you love doing and to seeing the people you love seeing.</p>
</div>

<!-- insights -->
<h2 class="abs heading insight-title">Latest Insight &amp; Thoughts</h2>
<div class="abs pattern" style="left:1100px;top:2630px;width:100px;height:230px" role="img" aria-label="Faint dotted pattern"></div>
<div class="abs pattern" style="left:0;top:2920px;width:70px;height:170px" role="img" aria-label="Faint dotted pattern"></div>
<article class="post" style="left:104px">
  <div class="post-img" role="img" aria-label="Photo of an estate agent showing a couple a property for sale sign" style="background:linear-gradient(120deg,#b0623c,#d9a27a 45%,#7a4a32)"></div>
  <h3>Spring Statement – Property Market Update – What does it mean for the property prices?</h3>
  <p>Raging Inflation...Covid...Brexit...war in Ukraine...and Tax Receipts rising! How can this be and what does it mean for you as a business owner or Property Investor? Ravi talks us through what this all means for business owners and the property market.</p>
  <span class="more">READ MORE</span>
</article>
<article class="post" style="left:626px">
  <div class="post-img" role="img" aria-label="Photo of two businessmen talking outside an office building" style="background:linear-gradient(120deg,#7f8f88,#b9c3bd 45%,#3e4a52)"></div>
  <h3>5 Benefits Property Investors missed in the Chancellor's Spring Statement</h3>
  <p>Did you know there were 5 policies in the spring statement that affect property investors which many people missed. Were you one of them? Ravi Sandhu is back again for a deep dive into the Chancellor's Spring Statement and the</p>
  <span class="more">READ MORE</span>
</article>

<!-- feedback -->
<div class="abs feedback"></div>
<div class="abs reviewer">
  <div class="avatar" role="img" aria-label="Portrait photo of the reviewer"></div>
  <div class="role">Buisness Manager</div>
  <div class="name">HARRIET</div>
</div>
<h2 class="abs heading fb-title">Clients Feedback</h2>
<p class="abs fb-quote">My experience with Tovelbrook Accountants has been second to none. They have been our business &amp; personal accountants for several years, always providing a highly efficient professional, reliable and friendly service. They have an</p>
<svg class="abs stars" width="150" height="24" viewBox="0 0 150 24" fill="#f3d35a" aria-label="5 stars"><g id="star"><path d="M12 1l3.2 7 7.6.8-5.7 5.1 1.7 7.5L12 17.6 5.2 21.4l1.7-7.5L1.2 8.8 8.8 8z"/></g><use href="#star" x="30"/><use href="#star" x="60"/><use href="#star" x="90"/><use href="#star" x="120"/></svg>
<div class="abs pager"><span></span><span class="on"></span><span></span></div>

<!-- cta -->
<div class="abs cta"></div>
<h2 class="abs heading cta-title">Set A Date Today To Speak To Our Team</h2>
<p class="abs cta-sub">Book An Appointment</p>
<div class="btn btn-white" style="left:838px;top:3681px;width:163px;height:41px">Book Now</div>

<!-- footer -->
<footer>
<div class="abs footer"></div>
<svg class="abs" style="left:0;top:3880px" width="160" height="125" aria-hidden="true"><polygon points="0,12 150,125 0,125" fill="var(--teal)"/></svg>
<div class="abs brand" style="left:90px;top:3810px;color:var(--white)"><span class="brand-mark"></span>Tovelbrook<br>Accountants</div>
<div class="abs foot-contact" style="top:3874px">
  <svg width="16" height="12" viewBox="0 0 16 12" fill="none" stroke="#fff" stroke-width="1.5"><rect x="1" y="1" width="14" height="10"/><path d="M1 1l7 6 7-6"/></svg>01632 960418</div>
<div class="abs foot-contact" style="top:3901px">
  <svg width="16" height="16" viewBox="0 0 16 16" fill="#fff"><path d="M8 0a6 6 0 0 1 6 6c0 4-6 10-6 10S2 10 2 6a6 6 0 0 1 6-6zm0 3.5A2.5 2.5 0 1 0 8 8.5 2.5 2.5 0 0 0 8 3.5z"/></svg>info@tovelbrookaccountants.co.uk</div>
<div class="abs foot-contact" style="top:3929px">
  <svg width="16" height="16" viewBox="0 0 16 16" fill="#fff"><path d="M3 1l3 3-2 2c1 2 3 4 6 6l2-2 3 3-2 2C7 15 1 9 1 3z"/></svg>14 Mill Lane, Harbridge, HB2 4QT</div>
<h4 class="abs foot-head" style="left:531px;top:3818px">Quick Link</h4>
<a class="abs foot-link" style="top:3862px">About Us</a>
<a class="abs foot-link" style="top:3884px">Who We Help</a>
<a class="abs foot-link" style="top:3906px">Thoughts</a>
<a class="abs foot-link" style="top:3928px">Switching Accountants</a>
<h4 class="abs foot-head" style="left:822px;top:3826px">Get In Touch</h4>
<div class="abs email">Email address</div>
<div class="abs signup">SIGN UP</div>
<div class="abs foot-rule"></div>
<p class="abs foot-bottom" style="left:479px">© 2023 Northlane. All rights reserved</p>
<p class="abs foot-bottom" style="left:799px">Terms &amp; Conditions</p>
<p class="abs foot-bottom" style="left:991px">Privacy &amp; Policy</p>
</footer>

</body>
</html>
```